Business Card Design Project

Looking for a business card that our customers will remember. We are a high end Travel Agency.
Need a re-memorable classy business card.
Both sides full color.
Must have the following details.
Voyage Harbor Logo (see attached)
4B Wattle Lane
Penhurst Sydney NSW 2241
Phone: 02 9471 3652
Fax: 02 9563 4417
sales@voyageharbor-example.com.au
Consultant Name
Anything else you think we need

```html
<!DOCTYPE html>
<html lang="en">
<head>
<meta charset="utf-8">
<title>Voyage Harbor Business Card</title>
<link rel="stylesheet" href="https://fonts.googleapis.com/css2?family=Open+Sans:wght@400;600;700&display=swap">
<style>
  :root {
    --backdrop-top: #6f6f6f;
    --backdrop-bottom: #d9d9d9;
    --card-white: #ffffff;
    --card-grey: #e6e6e6;
    --ocean-light: #5b8cb3;
    --ocean-deep: #1d5884;
    --label-blue: #2d6b97;
    --sun-yellow: #f3c623;
    --ink: #3a3a3a;
  }
  html, body {
    margin: 0;
    width: 1200px;
    height: 861px;
    overflow: hidden;
  }
  body {
    background: linear-gradient(var(--backdrop-top), var(--backdrop-bottom));
    font-family: "Open Sans", Arial, sans-serif;
  }
  .business-card {
    position: absolute;
    left: 240px;
    top: 210px;
    width: 720px;
    height: 440px;
    background: linear-gradient(160deg, var(--card-white) 45%, var(--card-grey));
    box-shadow: 0 18px 40px rgba(0,0,0,0.35);
    overflow: hidden;
  }
  .header-band {
    position: absolute;
    left: 0;
    top: 0;
    width: 100%;
    height: 140px;
    background: linear-gradient(135deg, var(--ocean-light), var(--ocean-deep));
  }
  .accent-rule {
    position: absolute;
    left: 0;
    top: 146px;
    width: 100%;
    height: 6px;
    background: var(--sun-yellow);
  }
  .consultant-name {
    position: absolute;
    right: 40px;
    top: 40px;
    margin: 0;
    color: var(--card-white);
    font-size: 34px;
    font-weight: 700;
  }
  .contact-list {
    position: absolute;
    left: 45px;
    top: 222px;
    margin: 0;
    font-size: 17px;
    line-height: 25px;
    color: var(--ink);
  }
  .contact-row {
    display: grid;
    grid-template-columns: 112px auto;
  }
  .contact-row dt {
    color: var(--label-blue);
    font-weight: 700;
  }
  .contact-row dd { margin: 0; }
  .contact-row.address { margin-bottom: 25px; }
  .brand {
    position: absolute;
    right: 40px;
    top: 296px;
    display: flex;
    align-items: center;
    gap: 10px;
    color: var(--label-blue);
    font-size: 24px;
    font-weight: 600;
  }
  .brand-dot {
    width: 14px;
    height: 14px;
    border-radius: 50%;
    background: var(--sun-yellow);
  }
</style>
</head>
<body>
  <article class="business-card">
    <div class="header-band"></div>
    <div class="accent-rule"></div>

    <h1 class="consultant-name">Consultant Name</h1>

    <dl class="contact-list">
      <div class="contact-row address">
        <dt>[Address]</dt>
        <dd>4B Wattle Lane Penhurst<br>Sydney NSW 2241</dd>
      </div>
      <div class="contact-row">
        <dt>[Telephone]</dt>
        <dd>02 9471 3652</dd>
      </div>
      <div class="contact-row">
        <dt>[Fax]</dt>
        <dd>02 9563 4417</dd>
      </div>
      <div class="contact-row">
        <dt>[E-mail]</dt>
        <dd>sales@voyageharbor-example.com.au</dd>
      </div>
    </dl>

    <div class="brand">
      <span>Voyage Harbor</span>
      <span class="brand-dot"></span>
    </div>
  </article>
</body>
</html>
```